Harcourt Meat Co. Card Design

Industry/Entity Type

Business

Contact Information for Business Card

Front
47b fernhill road Kelvale north vic 3871, Greg Harcourt ph 0352918406 mobile 0400583916,

Back
Local quality black angus
Home deliveries
Bulk pack specials
Wholesale available
Private animals cut and packed

Requirements
Must have
• Bullshead to be metallic silver colour like the silver on 1 of the pictured business cards

Flatblack back ground as seen on both business card pictures

Looking alot like the 2 pictured cards nice and neat

```html
<!DOCTYPE html>
<html lang="en">
<head>
<meta charset="utf-8">
<title>Harcourt Meat Co. – Business Card</title>
<link rel="stylesheet" href="https://fonts.googleapis.com/css2?family=Lato:wght@400;700&family=Montserrat:wght@700&display=swap">
<style>
  :root {
    --backdrop: #d9d9d9;
    --card-black: #141414;
    --emblem-grey: #262626;
    --accent-red: #e0262b;
    --silver: #c9c9c9;
    --contact-grey: #b5b5b5;
  }
  * { box-sizing: border-box; margin: 0; padding: 0; }
  html, body { width: 1200px; height: 747px; overflow: hidden; }
  body {
    background: var(--backdrop);
    font-family: "Lato", sans-serif;
    position: relative;
  }
  .card {
    position: absolute;
    top: 218px;
    width: 540px;
    height: 310px;
    background: var(--card-black);
    overflow: hidden;
    box-shadow: 0 6px 18px rgba(0,0,0,0.25);
  }
  .card--services { left: 45px; }
  .card--contact { left: 615px; }

  /* Services side */
  .emblem-area {
    position: absolute;
    left: 30px;
    top: 14px;
    width: 360px;
    height: 282px;
    border-radius: 50%;
    background: radial-gradient(circle, var(--emblem-grey) 0%, rgba(38,38,38,0.6) 60%, rgba(20,20,20,0) 100%);
  }
  .service-list {
    position: absolute;
    left: 40px;
    top: 118px;
    list-style: none;
    font-family: "Montserrat", sans-serif;
    font-weight: 700;
    font-variant: small-caps;
    font-size: 20px;
    letter-spacing: 1.5px;
    color: var(--accent-red);
  }
  .service-list li {
    display: flex;
    align-items: center;
    height: 32px;
    white-space: nowrap;
  }
  .service-list li::before {
    content: "";
    width: 14px;
    height: 14px;
    border-radius: 50%;
    background: var(--accent-red);
    margin-right: 18px;
    flex-shrink: 0;
  }

  /* Contact side */
  .brand {
    position: absolute;
    left: 30px;
    top: 34px;
    display: flex;
    align-items: center;
    gap: 12px;
    color: var(--silver);
    font-size: 22px;
    font-weight: 700;
    letter-spacing: 1px;
  }
  .brand-mark {
    width: 44px;
    height: 44px;
    border-radius: 50%;
    background: var(--silver);
  }
  .contact-list {
    position: absolute;
    left: 30px;
    top: 124px;
    list-style: none;
    color: var(--contact-grey);
    font-size: 17px;
    line-height: 1.2;
  }
  .contact-list li {
    display: flex;
    align-items: flex-start;
    margin-bottom: 10px;
    white-space: nowrap;
  }
  .contact-icon {
    width: 20px;
    height: 20px;
    margin-right: 10px;
    flex-shrink: 0;
    background: var(--accent-red);
    border-radius: 2px;
  }
  .holder-name {
    position: absolute;
    right: 70px;
    top: 150px;
    color: var(--accent-red);
    font-size: 22px;
    font-weight: 400;
    white-space: nowrap;
  }
  .accent-band {
    position: absolute;
    left: 0;
    bottom: 0;
    width: 220px;
    height: 16px;
    background: var(--accent-red);
  }
</style>
</head>
<body>

  <section class="card card--services">
    <div class="emblem-area" role="img" aria-label="Faint brand emblem decoration"></div>
    <ul class="service-list">
      <li>Local quality black angus</li>
      <li>Home deliveries</li>
      <li>Bulk pack specials</li>
      <li>Wholesale available</li>
      <li>Private animals cut and packed</li>
    </ul>
  </section>

  <section class="card card--contact">
    <div class="brand">
      <span class="brand-mark"></span>
      <span class="brand-name">Harcourt Meat Co.</span>
    </div>

    <ul class="contact-list">
      <li>
        <svg class="contact-icon" viewBox="0 0 20 20" aria-hidden="true">
          <path d="M6 4l2.5 3-1.5 1.5c.8 1.8 2.2 3.2 4 4l1.5-1.5 3 2.5-1.5 2C9 15 5 11 4 6z" fill="#141414"/>
        </svg>
        <span>03 5291 8406</span>
      </li>
      <li>
        <svg class="contact-icon" viewBox="0 0 20 20" aria-hidden="true">
          <rect x="6.5" y="3.5" width="7" height="13" rx="1" fill="none" stroke="#141414" stroke-width="1.6"/>
          <circle cx="10" cy="14" r="0.9" fill="#141414"/>
        </svg>
        <span>04 0058 3916</span>
      </li>
      <li>
        <svg class="contact-icon" viewBox="0 0 20 20" aria-hidden="true">
          <path d="M10 3a4.5 4.5 0 0 0-4.5 4.5C5.5 11 10 17 10 17s4.5-6 4.5-9.5A4.5 4.5 0 0 0 10 3z" fill="#141414"/>
          <circle cx="10" cy="7.5" r="1.6" fill="#e0262b"/>
        </svg>
        <span>47b fernhill road Kelvale<br>north vic 3871</span>
      </li>
    </ul>

    <p class="holder-name">Greg Harcourt</p>
    <div class="accent-band"></div>
  </section>

</body>
</html>
```